Medical Company in need of Modern business card design for new Wound Care clinic.

Modern business card design for our Woundcare company. Logo and description of services can be found on our website; https://www.tornvel-skinheal.com/

```html
<!DOCTYPE html>
<html lang="en">
<head>
<meta charset="UTF-8">
<title>Tornvel Skinheal – Business Card</title>
<link href="https://fonts.googleapis.com/css2?family=Montserrat:wght@400;500;700&family=Open+Sans:wght@400;600&display=swap" rel="stylesheet">
<style>
  :root {
    --backdrop: #d9dadb;
    --card: #ffffff;
    --gold: #c08a2e;
    --gold-light: #e3b65a;
    --ink: #141414;
    --edge: #1c1c1c;
    --tint: #fbf6ec;
  }
  * { margin: 0; padding: 0; box-sizing: border-box; }
  html, body {
    width: 1200px; height: 780px; overflow: hidden;
    background: var(--backdrop);
  }
  .canvas {
    position: relative; width: 1200px; height: 780px;
    display: flex; align-items: center; justify-content: center; gap: 24px;
  }
  .card {
    position: relative; width: 560px; height: 320px;
    background: var(--card); overflow: hidden;
    box-shadow: 0 10px 28px rgba(0,0,0,.25);
  }

  /* Front card */
  .front .brand {
    position: absolute; left: 34px; top: 60px;
    display: flex; align-items: center; gap: 12px;
    font-family: "Montserrat", sans-serif; font-weight: 500;
    font-size: 24px; letter-spacing: 5px; color: var(--ink);
  }
  .brand .mark-square {
    width: 18px; height: 18px; background: var(--gold);
  }
  .front .title-bar {
    position: absolute; right: 0; top: 22px; width: 46px; height: 22px;
    background: linear-gradient(90deg, var(--gold), var(--gold-light));
  }
  .front .person {
    position: absolute; right: 58px; top: 18px; text-align: right;
    font-family: "Montserrat", sans-serif;
  }
  .person .name { font-weight: 700; font-size: 28px; color: var(--gold); line-height: 1.1; }
  .person .role { font-weight: 500; font-size: 13px; color: var(--ink); }
  .front .rule {
    position: absolute; left: 34px; right: 150px; top: 126px;
    height: 1.5px; background: var(--gold);
  }
  .front .contact {
    position: absolute; left: 34px; top: 140px;
    font-family: "Open Sans", sans-serif; font-weight: 600;
    font-size: 13.5px; color: var(--ink); line-height: 1.45;
  }
  .contact .address { margin-bottom: 6px; }
  .contact ul { list-style: none; }
  .contact li { display: flex; align-items: center; gap: 8px; }
  .contact svg { width: 14px; height: 14px; fill: var(--gold); flex: none; }
  .front .base-band {
    position: absolute; left: 0; bottom: 0; width: 100%; height: 14px;
    background: linear-gradient(90deg, var(--gold), var(--gold-light) 40%, var(--gold) 62%, var(--edge) 62%);
  }

  /* Back card */
  .back { background: linear-gradient(160deg, var(--card) 45%, var(--tint)); }
  .back .brand-large {
    position: absolute; left: 0; right: 0; top: 88px; text-align: center;
    font-family: "Montserrat", sans-serif; font-weight: 500;
    font-size: 34px; letter-spacing: 8px; color: var(--ink);
  }
  .back .services {
    position: absolute; left: 36px; right: 36px; top: 168px; text-align: center;
    font-family: "Open Sans", sans-serif;
  }
  .services h2 {
    font-weight: 600; font-size: 15px; color: var(--gold); margin-bottom: 6px;
  }
  .services p { font-weight: 600; font-size: 12.5px; color: var(--ink); line-height: 1.6; }
  .services .dot {
    display: inline-block; width: 7px; height: 7px; border-radius: 50%;
    background: var(--gold); margin: 0 5px 1px 8px; vertical-align: middle;
  }
</style>
</head>
<body>
<main class="canvas">
  <section class="card front">
    <div class="brand"><span class="mark-square"></span>TORNVEL SKINHEAL</div>
    <div class="title-bar"></div>
    <div class="person">
      <div class="name">Delan Ostrik</div>
      <div class="role">Managing Director</div>
    </div>
    <div class="rule"></div>
    <div class="contact">
      <div class="address">2218 Marlow Ave Ste 40 PMB 118207<br>Dallas, TX 75204</div>
      <ul>
        <li><svg viewBox="0 0 24 24"><path d="M6.6 10.8a15 15 0 0 0 6.6 6.6l2.2-2.2a1 1 0 0 1 1-.25 11.4 11.4 0 0 0 3.6.57 1 1 0 0 1 1 1V20a1 1 0 0 1-1 1A17 17 0 0 1 3 4a1 1 0 0 1 1-1h3.5a1 1 0 0 1 1 1c0 1.25.2 2.45.57 3.57a1 1 0 0 1-.25 1z"/></svg>972-555-0147</li>
        <li><svg viewBox="0 0 24 24"><path d="M5 3h10v5H5zM3 9h18v10H3zm3 3v2h3v-2zm5 0v2h3v-2zm5 0v2h3v-2zM6 16v2h3v-2zm5 0v2h3v-2z"/></svg>(917) 555-0193</li>
        <li><svg viewBox="0 0 24 24"><path d="M12 2a10 10 0 1 0 0 20 10 10 0 0 0 0-20zm6.9 6h-3a15 15 0 0 0-1.3-3.9A8 8 0 0 1 18.9 8zM12 4c.8 1.2 1.5 2.5 1.9 4h-3.8c.4-1.5 1.1-2.8 1.9-4zM4.3 14a8 8 0 0 1 0-4h3.4a16 16 0 0 0 0 4zm.8 2h3a15 15 0 0 0 1.3 3.9A8 8 0 0 1 5.1 16zm3-8h-3a8 8 0 0 1 4.3-3.9A15 15 0 0 0 8.1 8zM12 20c-.8-1.2-1.5-2.5-1.9-4h3.8c-.4 1.5-1.1 2.8-1.9 4zm2.3-6H9.7a14 14 0 0 1 0-4h4.6a14 14 0 0 1 0 4zm.3 5.9a15 15 0 0 0 1.3-3.9h3a8 8 0 0 1-4.3 3.9zm1.7-5.9a16 16 0 0 0 0-4h3.4a8 8 0 0 1 0 4z"/></svg>www.tornvel-skinheal.com</li>
        <li><svg viewBox="0 0 24 24"><path d="M3 5h18v14H3zm2 2v.5l7 4.5 7-4.5V7zm0 2.9V17h14V9.9l-7 4.5z"/></svg>info@tornvel-skinheal.com</li>
      </ul>
    </div>
    <div class="base-band"></div>
  </section>

  <section class="card back">
    <div class="brand-large">TORNVEL SKINHEAL</div>
    <div class="services">
      <h2>OUR SERVICES</h2>
      <p>
        <span class="dot"></span>Hyperbaric Oxygen Therapy (HBO): A Cornerstone of Advanced Wound Care
        <span class="dot"></span>Debridement <span class="dot"></span>Advanced Wound Dressings
        <span class="dot"></span>Bio-engineered Skin Substitutes
        <span class="dot"></span>Compression Therapy <span class="dot"></span>and Edema Management
      </p>
    </div>
  </section>
</main>
</body>
</html>
```